Flyer redesign

We need this flier {Seasonal Care back 2018} redesigned for our 2019 season. It is attached below. New design should look different from current design. Be creative yet still professional.

Requirements
Must have
• Designed in photoshop.
• Should have the same text as current design. Only is "2019" instead of 2018. We want a different look with same info to send our customers next year.
• size: standard letter paper 8.5" x 11"
Nice to have
• Can use optional images provided. Not required though. See our website for more photos. thornbrookmemorial.org. send message through briskdrafts if you want a specific photo.
Should not have
• Do not take current design and just change date or image. Make the design look different.

```html
<!DOCTYPE html>
<html lang="en">
<head>
<meta charset="utf-8">
<title>2019 Gravesite Landscaping Packages – Thornbrook Memorial</title>
<link rel="stylesheet" href="https://fonts.googleapis.com/css2?family=Roboto+Condensed:wght@400;700&display=swap">
<style>
:root{
  --maroon:#6e1a1f;
  --maroon-deep:#5c1216;
  --olive:#a29d5e;
  --cream:#ebe8cf;
  --paper:#ffffff;
  --mist:#d8d8d6;
  --ink:#1d1d1d;
}
*{box-sizing:border-box;margin:0;padding:0}
html,body{width:927px;height:1200px;overflow:hidden;background:var(--paper)}
body{font-family:"Roboto Condensed",Arial,sans-serif;color:var(--ink)}
.flyer{position:relative;width:927px;height:1200px;background:linear-gradient(#e4e4e2,var(--mist))}
.hero-photo{position:absolute;left:0;top:0;width:927px;height:560px;
  background:linear-gradient(180deg,#c9d4c2 0%,#9fb08c 35%,#6f8754 60%,#8f9a86 80%,#c8c8c4 100%)}
.brand-bar{position:absolute;left:0;top:0;width:927px;height:103px;background:rgba(255,255,255,.72);
  display:flex;align-items:center;justify-content:center;gap:12px}
.brand-mark{width:18px;height:18px;background:var(--maroon)}
.brand-name{font-size:26px;letter-spacing:3px;color:var(--maroon);font-weight:400;text-transform:uppercase}
.title-badge{position:absolute;left:60px;top:215px;width:360px;height:260px}
.title-badge svg{position:absolute;inset:0}
.title-text{position:absolute;inset:0;display:flex;flex-direction:column;align-items:center;justify-content:center;text-align:center;color:var(--maroon-deep)}
.title-year{font-size:64px;font-weight:400;line-height:1}
.title-line{font-size:38px;line-height:1.12}

.footer-band{position:absolute;left:0;top:1094px;width:927px;height:106px;background:var(--maroon);
  display:flex;align-items:flex-end;justify-content:space-between;padding:0 30px 24px;color:#fff;font-size:18px}

.package{position:absolute;top:553px;width:295px;z-index:2}
.package-head{height:124px;background:var(--olive);border-radius:14px 14px 0 0;text-align:center;padding-top:3px}
.package-name{font-size:29px;font-weight:400;line-height:30px;color:var(--maroon);text-transform:uppercase}
.package-tag{font-size:18px;line-height:27px;color:var(--cream);margin-top:4px}
.package-body{position:relative;height:440px;background:var(--paper)}
.features{position:absolute;top:19px;list-style:none}
.features li{position:relative;padding-left:22px;font-size:16px;line-height:22.5px;margin-bottom:6px}
.features.tight li{line-height:21.5px;margin-bottom:0}
.features li::before{content:"";position:absolute;left:0;top:5px;width:12px;height:12px;border-radius:50%;background:var(--maroon)}
.features li::after{content:"";position:absolute;left:2.5px;top:8.5px;width:4px;height:4px;border-right:2px solid #fff;border-bottom:2px solid #fff;transform:rotate(-45deg)}
.price-block{position:absolute}
.term{font-size:19px;line-height:31px}
.price{font-size:36px;font-weight:400;color:var(--maroon);line-height:31px}
.note{position:absolute;font-size:16px;line-height:21px}
.basic .term{line-height:24px}
.basic .price{line-height:36px}
.perpetual .term{line-height:26px}
.perpetual .price{line-height:30px}
.basic .note{line-height:22.5px}
</style>
</head>
<body>
<div class="flyer">
  <div class="hero-photo" role="img" aria-label="Photograph of a cemetery path lined with headstones, trimmed hedges and trees"></div>

  <header class="brand-bar">
    <span class="brand-mark"></span>
    <span class="brand-name">Thornbrook Memorial</span>
  </header>

  <div class="title-badge">
    <svg width="360" height="260" viewBox="0 0 360 260">
      <rect x="30" y="25" width="290" height="210" rx="14" fill="rgba(162,157,94,.55)" stroke="#6e1a1f" stroke-width="3" transform="rotate(-8 175 130)"/>
      <rect x="40" y="30" width="280" height="200" rx="14" fill="rgba(168,160,100,.85)" stroke="#6e1a1f" stroke-width="3" transform="rotate(6 180 130)"/>
    </svg>
    <div class="title-text">
      <div class="title-year">2019</div>
      <div class="title-line">Gravesite</div>
      <div class="title-line">Landscaping</div>
      <div class="title-line">Packages</div>
    </div>
  </div>

  <footer class="footer-band">
    <span>info@thornbrookmemorial.org</span>
    <span>(555) 214-0387</span>
    <span>www.thornbrookmemorial.com</span>
  </footer>

  <section class="package seasonal" style="left:12px">
    <div class="package-head">
      <h2 class="package-name">Seasonal<br>Care</h2>
      <p class="package-tag">Seasonal landscaping<br>grave care.</p>
    </div>
    <div class="package-body">
      <ul class="features" style="left:14px">
        <li>Weeding and trimming<br>service on your gravesite<br>approximately every 7<br>weeks during the growing<br>season: mid-April through<br>mid-October</li>
      </ul>
      <div class="price-block" style="top:186px;left:96px">
        <div class="term">3 YEARS</div><div class="price">$327</div>
        <div class="term">2 YEARS</div><div class="price">$218</div>
        <div class="term">1YEAR</div><div class="price">$109</div>
      </div>
      <p class="note" style="top:388px;left:59px">Multi-year payment<br>locks in current rates.</p>
    </div>
  </section>

  <section class="package basic" style="left:321px">
    <div class="package-head">
      <h2 class="package-name">Basic Care<br>Endowment</h2>
      <p class="package-tag">Landscaping care forever<br>for graves with no plantings</p>
    </div>
    <div class="package-body">
      <ul class="features" style="left:12px">
        <li>Weeding and trimming<br>services on your gravesite<br>2 times per year: mid-May<br>and mid-September<br>Monument leveling</li>
        <li>Payment ensures grave<br>care forever</li>
      </ul>
      <div class="price-block" style="top:231px;left:68px">
        <div class="term">12 MONTHLY<br>PAYMENT OF</div>
        <div class="price">$225.00*</div>
      </div>
      <p class="note" style="top:324px;left:38px">*gravesite with single<br>headstones.Call for other<br>monument types and single<br>payement discount.<br>Valid through 10/31/2019</p>
    </div>
  </section>

  <section class="package perpetual" style="left:626px">
    <div class="package-head">
      <h2 class="package-name">Perpetual Care<br>Endowement</h2>
      <p class="package-tag">Landscaping care forever for<br>graves with plantings.</p>
    </div>
    <div class="package-body">
      <ul class="features tight" style="left:12px">
        <li>Weeding and trimming<br>services on your gravesite<br>approximately every 7<br>weeks during the growing<br>season: mid-April through<br>mid-October</li>
        <li>Monument leveling<br>and Cleaning</li>
        <li>Payment ensures grave<br>care forever</li>
        <li>Full bed of boxwood shrubs</li>
        <li>Replacement of shrubs</li>
        <li>Trust certificate</li>
      </ul>
      <div class="price-block" style="top:301px;left:67px;width:160px;text-align:center">
        <div class="term">12 MONTHLY<br>PAYMENTS OF</div>
        <div class="price">$280.42</div>
      </div>
      <p class="note" style="top:384px;left:27px">Call for single payment discount.<br>Valid through 10/31/2019.</p>
    </div>
  </section>
</div>
</body>
</html>
```